Step and Repeat Backdrop for wedding reception photo booth

Would like to have a Step and Repeat Backdrop (8 foot high by 10 foot wide) that incorporates the wedding logo (attached) and the names Elena and Gavin. Background should be white, and wedding colors are burgundy and gold. Show me creativity :-) I have included some random samples.

```html
<!DOCTYPE html>
<html lang="en">
<head>
<meta charset="utf-8">
<title>Elena &amp; Gavin — Step and Repeat Backdrop</title>
<link rel="stylesheet" href="https://fonts.googleapis.com/css2?family=Noto+Serif:wght@400&family=Playfair+Display:wght@500&display=swap">
<style>
  :root {
    --frame-black: #000000;
    --paper: #f8f4ea;
    --paper-deep: #efe6d2;
    --burgundy: #7a0a12;
    --burgundy-dark: #4a0a10;
    --gold: #a9802f;
    --gold-light: #d8bf86;
    --gold-pale: #e6d5ab;
    --repeat-rose: rgba(196, 120, 120, 0.45);
  }
  * { margin: 0; padding: 0; box-sizing: border-box; }
  html, body { width: 1200px; height: 900px; overflow: hidden; background: var(--frame-black); }
  .canvas { position: relative; width: 1200px; height: 900px; background: var(--frame-black); }
  .backdrop {
    position: absolute; left: 126px; top: 71px; width: 948px; height: 758px;
    background: radial-gradient(ellipse at 50% 40%, var(--paper) 0%, var(--paper) 45%, var(--paper-deep) 100%);
    overflow: hidden;
  }
  .paisley-field {
    position: absolute; inset: 0;
    background: linear-gradient(160deg, rgba(230,213,171,0.18), rgba(255,255,255,0) 50%, rgba(230,213,171,0.22));
  }
  .border-band {
    position: absolute;
    background: linear-gradient(90deg, var(--gold-pale), var(--gold-light), var(--gold-pale));
    opacity: 0.75;
    border-radius: 20px;
  }
  .border-band.top { left: 31px; top: 13px; width: 885px; height: 41px; }
  .border-band.bottom { left: 31px; top: 702px; width: 885px; height: 43px; }
  .border-band.left { left: 12px; top: 43px; width: 44px; height: 676px;
    background: linear-gradient(180deg, var(--gold-pale), var(--gold-light), var(--gold-pale)); }
  .border-band.right { left: 892px; top: 43px; width: 44px; height: 676px;
    background: linear-gradient(180deg, var(--gold-pale), var(--gold-light), var(--gold-pale)); }

  .repeat-mark {
    position: absolute; width: 70px; margin-left: -35px; margin-top: -20px;
    text-align: center;
    font-family: "Playfair Display", serif; font-weight: 500; font-size: 30px; line-height: 40px;
    color: var(--repeat-rose);
    transform: rotate(-30deg);
  }

  .couple-names { position: absolute; left: 0; top: 0; width: 948px; height: 758px; }
  .couple-names text {
    font-family: "Noto Serif", serif; font-size: 82px; letter-spacing: 2px;
  }

  .monogram-flourish {
    position: absolute; left: 322px; width: 303px;
    background: linear-gradient(90deg, var(--gold-pale), var(--gold), var(--gold-pale));
    opacity: 0.8; border-radius: 50px;
  }
  .monogram-flourish.upper { top: 219px; height: 98px; }
  .monogram-flourish.lower { top: 442px; height: 95px; }
  .monogram {
    position: absolute; left: 322px; top: 318px; width: 303px;
    text-align: center;
    font-family: "Playfair Display", serif; font-weight: 500; font-size: 118px; line-height: 124px;
    color: var(--gold);
  }
</style>
</head>
<body>
<div class="canvas">
  <div class="backdrop">
    <div class="paisley-field" role="img" aria-label="Soft cream paisley pattern background"></div>

    <div class="border-band top" role="img" aria-label="Gold scrollwork border"></div>
    <div class="border-band bottom" role="img" aria-label="Gold scrollwork border"></div>
    <div class="border-band left" role="img" aria-label="Gold scrollwork border"></div>
    <div class="border-band right" role="img" aria-label="Gold scrollwork border"></div>

    <div class="repeat-grid" aria-hidden="true">
      <span class="repeat-mark" style="left:115px;top:103px">E&amp;G</span>
      <span class="repeat-mark" style="left:235px;top:103px">E&amp;G</span>
      <span class="repeat-mark" style="left:354px;top:103px">E&amp;G</span>
      <span class="repeat-mark" style="left:474px;top:103px">E&amp;G</span>
      <span class="repeat-mark" style="left:596px;top:103px">E&amp;G</span>
      <span class="repeat-mark" style="left:715px;top:103px">E&amp;G</span>
      <span class="repeat-mark" style="left:837px;top:103px">E&amp;G</span>

      <span class="repeat-mark" style="left:115px;top:195px">E&amp;G</span>
      <span class="repeat-mark" style="left:235px;top:195px">E&amp;G</span>
      <span class="repeat-mark" style="left:354px;top:195px">E&amp;G</span>
      <span class="repeat-mark" style="left:474px;top:195px">E&amp;G</span>
      <span class="repeat-mark" style="left:596px;top:195px">E&amp;G</span>
      <span class="repeat-mark" style="left:715px;top:195px">E&amp;G</span>
      <span class="repeat-mark" style="left:837px;top:195px">E&amp;G</span>

      <span class="repeat-mark" style="left:115px;top:287px">E&amp;G</span>
      <span class="repeat-mark" style="left:235px;top:287px">E&amp;G</span>
      <span class="repeat-mark" style="left:715px;top:287px">E&amp;G</span>
      <span class="repeat-mark" style="left:837px;top:287px">E&amp;G</span>

      <span class="repeat-mark" style="left:115px;top:379px">E&amp;G</span>
      <span class="repeat-mark" style="left:235px;top:379px">E&amp;G</span>
      <span class="repeat-mark" style="left:715px;top:379px">E&amp;G</span>
      <span class="repeat-mark" style="left:837px;top:379px">E&amp;G</span>

      <span class="repeat-mark" style="left:115px;top:472px">E&amp;G</span>
      <span class="repeat-mark" style="left:235px;top:472px">E&amp;G</span>
      <span class="repeat-mark" style="left:715px;top:472px">E&amp;G</span>
      <span class="repeat-mark" style="left:837px;top:472px">E&amp;G</span>

      <span class="repeat-mark" style="left:115px;top:564px">E&amp;G</span>
      <span class="repeat-mark" style="left:235px;top:564px">E&amp;G</span>
      <span class="repeat-mark" style="left:354px;top:564px">E&amp;G</span>
      <span class="repeat-mark" style="left:474px;top:564px">E&amp;G</span>
      <span class="repeat-mark" style="left:596px;top:564px">E&amp;G</span>
      <span class="repeat-mark" style="left:715px;top:564px">E&amp;G</span>
      <span class="repeat-mark" style="left:837px;top:564px">E&amp;G</span>

      <span class="repeat-mark" style="left:115px;top:656px">E&amp;G</span>
      <span class="repeat-mark" style="left:235px;top:656px">E&amp;G</span>
      <span class="repeat-mark" style="left:354px;top:656px">E&amp;G</span>
      <span class="repeat-mark" style="left:474px;top:656px">E&amp;G</span>
      <span class="repeat-mark" style="left:596px;top:656px">E&amp;G</span>
      <span class="repeat-mark" style="left:715px;top:656px">E&amp;G</span>
      <span class="repeat-mark" style="left:837px;top:656px">E&amp;G</span>
    </div>

    <svg class="couple-names" viewBox="0 0 948 758" xmlns="http://www.w3.org/2000/svg">
      <defs>
        <linearGradient id="name-tone" x1="0" y1="0" x2="1" y2="0">
          <stop offset="0" stop-color="var(--burgundy)"/>
          <stop offset="0.35" stop-color="var(--burgundy-dark)"/>
          <stop offset="1" stop-color="var(--burgundy)"/>
        </linearGradient>
        <path id="name-arc" d="M 61,567 A 423 423 0 0 1 907,567" fill="none"/>
      </defs>
      <text fill="url(#name-tone)" text-anchor="middle">
        <textPath href="#name-arc" startOffset="50%">Elena &amp; Gavin</textPath>
      </text>
    </svg>

    <div class="monogram-flourish upper" role="img" aria-label="Gold flourish ornament above monogram"></div>
    <div class="monogram">E&amp;G</div>
    <div class="monogram-flourish lower" role="img" aria-label="Gold flourish ornament below monogram"></div>
  </div>
</div>
</body>
</html>
```